Modern, upmarket label design for food product

We need a label design for a food company producing nuts with sesame and honey. In fact, we would like the words "Cashews med sesam & honning" on the label (It's in Danish and means - Cashews with sesame & honey). It should be easy for the customer to quickly understand what it is.

It is a shelf product in the competitive food industry, which is why the design should wake the feeling of 'just wanting to grab the product down from the shelves'. So, the design should stand out and have an image of a cool, modern, hip product. This being said, I love a raw & handmade look.

The company is called Pølle. Its origins are from the danish word Tiks that is a Danish slang for yummy. I have uploaded a photo of the package the products will be sold in.

Info & dimensions on bag in picture 1.
Dimensions: 6" x 9" | 15.2 cm x 22.3 cm
Capacity: 8 ounces | 250 grams (based on whole bean coffee)

Picture 2 is the same product, but has the possibility of attaching to a hanger on shelfs.

Picture 3 - I have also uploaded a photo of a product bag, where the hole is linear instead of a round hole. The designer chooses, which bag they will like to work with!

Please let me know if there are any questions!

Target Market(s)

Target market could really be any age, but the design needs to compel the target audience to pick it from the shelves. The package should signal a product you want to hold and have other people seeing you have it. The target audience is people who cares for what they buy, and typically doesn't want a low-end or budget product. They want the whole thing, meaning it has to taste good, look good etc. They are also the type of people who like to show off whatever products they buy by placing them in their houses for their guests to see. Or by uploading pictures of it on social medias.

Industry/Entity Type

It Company

Font styles to use
Other font styles liked:
• Not a must, but I like the 'Panton' script

Requirements
Must have
• My project must have the words 'Cashews med sesam & honning' on the label, so the customer will know within a second what they are looking at and buying.
Nice to have
• I am picturing the label with the words 'Cashews med sesam & honning' as a statement, again, emphasizing how the customer instantly should know what the product is. This being said, it should not be the only thing on the package and I love a raw & handmade look - which inspiration picture 5 is a great example of!
• I have uploaded photos of what I think looks good. With this said, I am not looking for a copy of those products, but see them as good inspiration. I have named the photos inspiration 1, 2, 3, 4 & 5.
• If needed, more text can be put on the label. For example 'vegan', 'laktosefri', Glutenfri', or 'Sund Snack' are great words for being used on the label.
Should not have
• The fonts on the label should not be too decorative. Personally I like an easy too read font.

```html
<!DOCTYPE html>
<html lang="da">
<head>
<meta charset="utf-8">
<title>Pølle Cashews – label</title>
<link href="https://fonts.googleapis.com/css2?family=Passion+One:wght@400;700&family=Libre+Baskerville&family=Tinos:ital,wght@0,700;1,400;1,700&family=Lato:wght@400&display=swap" rel="stylesheet">
<style>
  :root {
    --backdrop: #d9c3a0;
    --label-cream: #f8f3dc;
    --ink-brown: #4a2511;
    --shadow: rgba(60, 35, 15, 0.18);
  }
  * { margin: 0; padding: 0; box-sizing: border-box; }
  html, body {
    width: 1200px; height: 1104px; overflow: hidden;
    background: var(--backdrop);
  }
  .canvas { position: relative; width: 1200px; height: 1104px; }

  .label {
    position: absolute; top: 122px; height: 860px;
    background: var(--label-cream);
    color: var(--ink-brown);
    box-shadow: 0 6px 18px var(--shadow);
  }
  .label--front { left: 90px; width: 510px; }
  .label--back { left: 680px; width: 430px; }

  .stripes { position: absolute; left: 0; display: block; }
  .stripes--top { top: 0; }
  .stripes--bottom { bottom: 0; }

  .centered {
    position: absolute; left: 0; right: 0; text-align: center;
  }

  .dot-rule {
    position: absolute; height: 10px;
    background: repeating-linear-gradient(90deg, var(--ink-brown) 0 3px, transparent 3px 13px);
  }

  /* front */
  .brand-name {
    top: 280px;
    font-family: "Passion One", sans-serif; font-weight: 400;
    font-size: 64px; line-height: 1; letter-spacing: 1px;
  }
  .product-name {
    top: 398px;
    font-family: "Passion One", sans-serif; font-weight: 700;
    font-size: 120px; line-height: 1; letter-spacing: -1px;
  }
  .flavour {
    font-family: "Libre Baskerville", serif;
    font-size: 42px; line-height: 1;
  }
  .flavour--first { top: 592px; }
  .flavour--second { top: 650px; }
  .claims {
    position: absolute; top: 756px; left: 20px; right: 20px;
    display: flex; justify-content: space-between;
    font-family: "Lato", sans-serif; font-size: 19px;
  }

  /* back */
  .info-heading {
    font-family: "Tinos", serif; font-weight: 700; font-style: italic;
    font-size: 28px; line-height: 1;
  }
  .info-text {
    font-family: "Tinos", serif; font-style: italic;
    font-size: 28px; line-height: 38px;
  }
  .net-weight {
    top: 682px;
    font-family: "Tinos", serif; font-weight: 700;
    font-size: 28px; line-height: 1;
  }
</style>
</head>
<body>
<main class="canvas">

  <section class="label label--front" aria-label="Front label">
    <svg class="stripes stripes--top" width="510" height="240" viewBox="0 0 510 240" aria-hidden="true">
      <g stroke="var(--ink-brown)" stroke-width="3.5">
        <line x1="112" y1="0" x2="112" y2="240"/><line x1="129" y1="0" x2="129" y2="240"/>
        <line x1="146" y1="0" x2="146" y2="240"/><line x1="163" y1="0" x2="163" y2="240"/>
        <line x1="180" y1="0" x2="180" y2="240"/><line x1="197" y1="0" x2="197" y2="240"/>
        <line x1="214" y1="0" x2="214" y2="240"/><line x1="231" y1="0" x2="231" y2="240"/>
        <line x1="248" y1="0" x2="248" y2="240"/><line x1="265" y1="0" x2="265" y2="240"/>
        <line x1="282" y1="0" x2="282" y2="240"/><line x1="299" y1="0" x2="299" y2="240"/>
        <line x1="316" y1="0" x2="316" y2="240"/><line x1="333" y1="0" x2="333" y2="240"/>
        <line x1="350" y1="0" x2="350" y2="240"/><line x1="367" y1="0" x2="367" y2="240"/>
        <line x1="384" y1="0" x2="384" y2="240"/><line x1="401" y1="0" x2="401" y2="240"/>
      </g>
    </svg>

    <h2 class="centered brand-name">Pølle</h2>
    <div class="dot-rule" style="top:370px; left:106px; width:296px;"></div>
    <h1 class="centered product-name">Cashews</h1>
    <p class="centered flavour flavour--first">med sesam</p>
    <p class="centered flavour flavour--second">&amp; honning</p>
    <div class="dot-rule" style="top:712px; left:106px; width:296px;"></div>
    <ul class="claims" style="list-style:none;">
      <li>Sund Snack</li><li>Glutenfri</li><li>Vegan</li><li>Laktosfri</li>
    </ul>

    <svg class="stripes stripes--bottom" width="510" height="50" viewBox="0 0 510 50" aria-hidden="true">
      <g stroke="var(--ink-brown)" stroke-width="3.5">
        <line x1="112" y1="0" x2="112" y2="50"/><line x1="129" y1="0" x2="129" y2="50"/>
        <line x1="146" y1="0" x2="146" y2="50"/><line x1="163" y1="0" x2="163" y2="50"/>
        <line x1="180" y1="0" x2="180" y2="50"/><line x1="197" y1="0" x2="197" y2="50"/>
        <line x1="214" y1="0" x2="214" y2="50"/><line x1="231" y1="0" x2="231" y2="50"/>
        <line x1="248" y1="0" x2="248" y2="50"/><line x1="265" y1="0" x2="265" y2="50"/>
        <line x1="282" y1="0" x2="282" y2="50"/><line x1="299" y1="0" x2="299" y2="50"/>
        <line x1="316" y1="0" x2="316" y2="50"/><line x1="333" y1="0" x2="333" y2="50"/>
        <line x1="350" y1="0" x2="350" y2="50"/><line x1="367" y1="0" x2="367" y2="50"/>
        <line x1="384" y1="0" x2="384" y2="50"/><line x1="401" y1="0" x2="401" y2="50"/>
      </g>
    </svg>
  </section>

  <section class="label label--back" aria-label="Back label">
    <svg class="stripes stripes--top" width="430" height="170" viewBox="0 0 430 170" aria-hidden="true">
      <g stroke="var(--ink-brown)" stroke-width="3.5">
        <line x1="46" y1="0" x2="46" y2="170"/><line x1="64" y1="0" x2="64" y2="170"/>
        <line x1="82" y1="0" x2="82" y2="170"/><line x1="100" y1="0" x2="100" y2="170"/>
        <line x1="118" y1="0" x2="118" y2="170"/><line x1="136" y1="0" x2="136" y2="170"/>
        <line x1="154" y1="0" x2="154" y2="170"/><line x1="172" y1="0" x2="172" y2="170"/>
        <line x1="190" y1="0" x2="190" y2="170"/><line x1="208" y1="0" x2="208" y2="170"/>
        <line x1="226" y1="0" x2="226" y2="170"/><line x1="244" y1="0" x2="244" y2="170"/>
        <line x1="262" y1="0" x2="262" y2="170"/><line x1="280" y1="0" x2="280" y2="170"/>
        <line x1="298" y1="0" x2="298" y2="170"/><line x1="316" y1="0" x2="316" y2="170"/>
        <line x1="334" y1="0" x2="334" y2="170"/><line x1="352" y1="0" x2="352" y2="170"/>
        <line x1="370" y1="0" x2="370" y2="170"/>
      </g>
    </svg>

    <h3 class="centered info-heading" style="top:276px;">Ingredients:</h3>
    <p class="centered info-text" style="top:330px;">Cashew, other ingredients<br>or whatever text needs to<br>be here</p>
    <div class="dot-rule" style="top:476px; left:104px; width:240px;"></div>
    <h3 class="centered info-heading" style="top:512px;">Manufactured by:</h3>
    <p class="centered info-text" style="top:546px;">Companu address phone<br>numbers and website</p>
    <div class="dot-rule" style="top:642px; left:104px; width:240px;"></div>
    <p class="centered net-weight">Net weight</p>
  </section>

</main>
</body>
</html>
```